7 3/4 x 5 1/4 Annual Banquet Invitation

Design an invitation for our Chamber's annual banquet. It will be a single sided invitation 5 1/4" wide by 7 3/4" height that we will print in-house. Our logo is attached. The theme is "Serving Together". I was thinking of an image with two hands coming together in a handshake, perhaps intertwining our logo colors. This is just a thought. I am open for any suggestions! Text for the invitation should be as follows: The Board of Directors and Staff cordially invites you to attend the 64th Yearly Gathering & Micro-Trade Fair - Monday, January 22, 2018. 5:30 p.m. Social, 6:00 p.m. Dinner. Cedarvale Chapel, 4819 Harlan P. Moss Rd S, Elmbrook. Please RSVP by January 18, 2018.

Target Market(s)

This invitation will be printed and mailed to our membership.

Industry/Entity Type

Business Management

Colors
33a6d7
faa54b
0355a3
00a990

Requirements
Must have
• Event info as indentified above.
Nice to have
• Our Logo

```html
<!DOCTYPE html>
<html lang="en">
<head>
<meta charset="utf-8">
<title>64th Yearly Gathering &amp; Micro-Trade Fair – Invitation</title>
<link href="https://fonts.googleapis.com/css2?family=Anton&family=Roboto+Condensed:wght@700&family=Lato:ital,wght@0,400;0,700;1,700&display=swap" rel="stylesheet">
<style>
  :root {
    --navy: #0355a3;
    --sky: #33a6d7;
    --orange: #faa54b;
    --teal: #00a990;
    --mint: #8ef07f;
    --white: #ffffff;
    --ink: #2b2b2b;
    --grey-dark: #b9b9b9;
    --grey-light: #d3d3d3;
    --brand-blue: #1f3f8f;
  }
  * { box-sizing: border-box; margin: 0; padding: 0; }
  html, body { width: 907px; height: 1200px; overflow: hidden; background: #ececec; }
  .invitation {
    position: relative;
    width: 907px;
    height: 1200px;
    overflow: hidden;
    background: radial-gradient(ellipse at 70% 40%, #4fb0e4 0%, var(--sky) 25%, #1c7cc3 60%, var(--navy) 100%);
    font-family: "Lato", sans-serif;
  }
  .backdrop { position: absolute; inset: 0; }
  .photo { position: absolute; border-radius: 50%; }
  .photo--handshake {
    left: 62px; top: 14px; width: 392px; height: 392px;
    background: radial-gradient(circle at 55% 50%, #e9c3a5 0%, #c9d0da 35%, #8a98ab 70%, #dfe4ea 100%);
  }
  .photo--audience {
    left: 706px; top: 445px; width: 350px; height: 350px;
    transform: translate(-50%, -50%);
    background: linear-gradient(180deg, #e7e9ee 0%, #b8bcc6 40%, #5b4a44 70%, #2f2a2a 100%);
  }
  .brand {
    position: absolute;
    left: 548px; top: 150px;
    display: flex; align-items: center; gap: 12px;
    font-family: "Lato", sans-serif;
    font-weight: 700;
    color: var(--brand-blue);
    white-space: nowrap;
  }
  .brand__dot { width: 36px; height: 36px; border-radius: 50%; background: var(--teal); flex: none; }
  .brand__name { font-size: 21px; line-height: 1.2; letter-spacing: 0.3px; text-transform: uppercase; }
  .welcome {
    position: absolute;
    left: 48px; top: 520px;
    font-family: "Roboto Condensed", sans-serif;
    font-weight: 700;
    font-size: 37px;
    line-height: 1.22;
    color: var(--mint);
  }
  .headline-band {
    position: absolute;
    left: 0; top: 672px; width: 907px; height: 170px;
    background: linear-gradient(90deg, rgba(255,255,255,0.12), rgba(255,255,255,0.04) 70%, rgba(255,255,255,0));
    border-top: 1px solid rgba(255,255,255,0.18);
    border-bottom: 1px solid rgba(255,255,255,0.18);
  }
  .headline {
    position: absolute;
    left: 46px; top: 686px;
    font-family: "Anton", sans-serif;
    font-weight: 400;
    font-size: 64px;
    line-height: 1.15;
    color: var(--orange);
    text-transform: uppercase;
    letter-spacing: 0.5px;
    text-shadow: 2px 3px 4px rgba(0,0,0,0.35);
  }
  .date {
    position: absolute;
    left: 46px; top: 855px;
    color: var(--white);
    font-weight: 700;
  }
  .date__day { font-size: 44px; line-height: 1.2; }
  .date__time { font-size: 32px; line-height: 1.3; }
  .footer { position: absolute; left: 0; top: 960px; width: 907px; height: 240px; }
  .rsvp {
    position: absolute;
    left: 46px; top: 1090px;
    font-style: italic; font-weight: 700;
    font-size: 27px; line-height: 1.3;
    color: var(--white);
  }
  .venue {
    position: absolute;
    right: 28px; top: 1048px;
    text-align: right;
    font-style: normal;
    font-size: 30px; font-weight: 400; line-height: 1.3;
    color: var(--ink);
    white-space: nowrap;
  }
</style>
</head>
<body>
  <main class="invitation">
    <svg class="backdrop" width="907" height="1200" viewBox="0 0 907 1200" aria-hidden="true">
      <path d="M0,0 H907 V250 C720,262 560,330 420,410 C330,462 220,480 130,440 C60,408 20,350 0,300 Z" fill="var(--white)"/>
      <path d="M250,440 C420,440 560,330 907,300" fill="none" stroke="var(--teal)" stroke-width="10"/>
      <path d="M230,452 C420,452 580,346 907,318" fill="none" stroke="var(--white)" stroke-width="8"/>
      <path d="M62,270 A200,200 0 0 0 440,300" fill="none" stroke="var(--orange)" stroke-width="7" transform="translate(0,14)"/>
      <circle cx="706" cy="445" r="182" fill="var(--white)"/>
      <path d="M560,560 A185,185 0 0 0 900,520" fill="none" stroke="var(--orange)" stroke-width="7"/>
    </svg>

    <div class="photo photo--handshake" role="img" aria-label="Photo of two business people shaking hands"></div>
    <div class="photo photo--audience" role="img" aria-label="Photo of an audience listening to a speaker at a business event"></div>

    <div class="brand">
      <span class="brand__dot"></span>
      <span class="brand__name">Harbor Ridge Chamber<br>of Commerce &amp; Tourism</span>
    </div>

    <p class="welcome">The Board of Directors<br>and Staff cordially invites<br>you to attend</p>

    <div class="headline-band"></div>
    <h1 class="headline">The 64th Yearly Gathering<br>&amp; Micro-Trade Fair</h1>

    <div class="date">
      <p class="date__day">Monday, January 22, 2018.</p>
      <p class="date__time">5:30 p.m. Social, 6:00 p.m. Dinner.</p>
    </div>

    <svg class="footer" width="907" height="240" viewBox="0 0 907 240" aria-hidden="true">
      <path d="M0,100 C250,70 560,20 907,55 V240 H0 Z" fill="var(--white)"/>
      <path d="M0,112 C250,82 560,34 907,68 V240 H0 Z" fill="var(--grey-light)"/>
      <rect x="0" y="115" width="418" height="125" fill="var(--grey-dark)"/>
      <path d="M418,88 V240" stroke="#ffffff" stroke-opacity="0.6" stroke-width="2"/>
    </svg>

    <p class="rsvp">Please RSVP by<br>January 18, 2018.</p>
    <address class="venue">Cedarvale Chapel,<br>4819 Harlan P. Moss Rd<br>S, Elmbrook.</address>
  </main>
</body>
</html>
```